Modern furniture store needs a catalogue in PDF

We need a catalogue design for a company based in Ecuador, South America called KESTRO. We have replica furniture and also authentic furniture from Europe which are classified in two separate ranges. KESTRO is the brand for designer replicas and THE VOLMERA HOUSE is for authentic designer furniture and house decoration. We would like to see a design that provides an idea of exclusivity and minimalistic design.

Target Market(s)

Upmarket families and new home owners from Ecuador, South America.

Industry/Entity Type

Furniture Store

Font styles to use
Sans Serif

Requirements
Must have
• A nice presentation of each furniture item.
• You can look for images on the internet for each product as they are designer items available all around the world. You can use images from the websites:
• www.kestro-example.net
• www.sondelo-example.com
• www.pirrola-example.fi
• The images don't need to be high resolution as the PDF will be sent electronically (i.e. via email) and not printed.
Nice to have
• Diagrams with the dimensions of each item so that clients understand how big they are.
• It could be in spanish, but I could also translate it after the design is finished.

```html
<!DOCTYPE html>
<html lang="es">
<head>
<meta charset="utf-8">
<title>KESTRO · Silloneria</title>
<link rel="stylesheet" href="https://fonts.googleapis.com/css2?family=Montserrat:wght@800&family=Arimo:wght@400&display=swap">
<style>
  :root {
    --backdrop: #e9e9e9;
    --paper: #ffffff;
    --band: #2b2523;
    --band-text: #ffffff;
    --ink: #1e1e1e;
    --rule: #3a3a3a;
    --photo-a: #f1f1f1;
    --photo-b: #dcdcdc;
  }
  * { box-sizing: border-box; margin: 0; padding: 0; }
  html, body { width: 1200px; height: 880px; overflow: hidden; }
  body {
    background: var(--backdrop);
    font-family: "Arimo", Arial, sans-serif;
    color: var(--ink);
  }
  .spread {
    position: absolute;
    left: 40px; top: 110px;
    width: 1120px; height: 660px;
    display: flex;
    box-shadow: 0 6px 24px rgba(0,0,0,.18);
  }
  .page {
    position: relative;
    width: 560px; height: 660px;
    background: var(--paper);
  }
  .page--left { background: linear-gradient(to right, var(--paper) 92%, #f0f0f0 100%); }
  .page--right { background: linear-gradient(to left, var(--paper) 92%, #ececec 100%); }
  .section-band {
    height: 50px;
    background: var(--band);
    display: flex; align-items: center;
    padding-left: 26px;
  }
  .section-title {
    font-family: "Montserrat", sans-serif;
    font-weight: 800;
    font-size: 17px;
    letter-spacing: .5px;
    color: var(--band-text);
  }
  .catalogue {
    display: grid;
    grid-template-columns: 1fr 1fr;
    column-gap: 14px;
    padding: 22px 20px 0 18px;
  }
  .column { display: flex; flex-direction: column; gap: 14px; }
  .product {
    display: flex; align-items: center; gap: 10px;
    height: 133px;
  }
  .product-photo {
    flex: 0 0 98px; height: 78px;
    border-radius: 3px;
    background: radial-gradient(ellipse at 50% 55%, var(--photo-b), var(--photo-a) 75%);
  }
  .product-photo--dark { background: radial-gradient(ellipse at 50% 55%, #4a4644, #e4e4e4 78%); }
  .product-photo--brown { background: radial-gradient(ellipse at 50% 55%, #5a3c30, #e6e1de 78%); }
  .product-photo--white { background: radial-gradient(ellipse at 50% 55%, #fafafa, #d9d9d9 85%); }
  .spec {
    flex: 1;
    border-top: 1px solid var(--rule);
    border-bottom: 1px solid var(--rule);
    padding: 6px 0 6px;
    display: grid;
    grid-template-columns: 58px 8px 1fr;
    font-size: 7.6px;
    line-height: 9.4px;
  }
  .spec dt { text-transform: uppercase; }
  .spec .sep::before { content: ":"; }
  .spec dd { margin: 0; }
  .spec .gap { grid-column: 1 / -1; height: 4px; }
</style>
</head>
<body>
<main class="spread">

  <section class="page page--left">
    <header class="section-band"><h1 class="section-title">SILLONERIA</h1></header>
    <div class="catalogue">
      <div class="column">
        <article class="product">
          <div class="product-photo product-photo--dark" role="img" aria-label="Foto: sillón Serrano Chair en cuero negro"></div>
          <dl class="spec"><dt>Marca</dt><span class="sep"></span><dd>KESTRO</dd><dt>Diseñador</dt><span class="sep"></span><dd>Anselm Varga 1929</dd><dt>Modelo</dt><span class="sep"></span><dd>Serrano Chair</dd><dt>Acabado</dt><span class="sep"></span><dd>Acero Inox. Frente C/ Natural, Reves C/ Artificial. Esponja A/D</dd><span class="gap"></span><dt>Medidas</dt><span class="sep"></span><dd>Ancho: 77 cms.<br>Fondo: 82 cms.<br>Altura: 76 cms</dd><span class="gap"></span><dt>Color</dt><span class="sep"></span><dd>Negro</dd></dl>
        </article>
        <article class="product">
          <div class="product-photo product-photo--white" role="img" aria-label="Foto: sillón Serrano Chair en cuero blanco"></div>
          <dl class="spec"><dt>Marca</dt><span class="sep"></span><dd>KESTRO</dd><dt>Diseñador</dt><span class="sep"></span><dd>Anselm Varga 1929</dd><dt>Modelo</dt><span class="sep"></span><dd>Serrano Chair</dd><dt>Acabado</dt><span class="sep"></span><dd>Acero Inox. Frente C/ Natural, Reves C/ Artificial. Esponja A/D</dd><span class="gap"></span><dt>Medidas</dt><span class="sep"></span><dd>Ancho: 77 cms.<br>Fondo: 82 cms.<br>Altura: 76 cms</dd><span class="gap"></span><dt>Color</dt><span class="sep"></span><dd>Blanco</dd></dl>
        </article>
        <article class="product">
          <div class="product-photo product-photo--brown" role="img" aria-label="Foto: sillón Serrano Chair en cuero café"></div>
          <dl class="spec"><dt>Marca</dt><span class="sep"></span><dd>KESTRO</dd><dt>Diseñador</dt><span class="sep"></span><dd>Anselm Varga 1929</dd><dt>Modelo</dt><span class="sep"></span><dd>Serrano Chair</dd><dt>Acabado</dt><span class="sep"></span><dd>Acero Inox. Frente C/ Natural, Reves C/ Artificial. Esponja A/D</dd><span class="gap"></span><dt>Medidas</dt><span class="sep"></span><dd>Ancho: 77 cms.<br>Fondo: 82 cms.<br>Altura: 76 cms</dd><span class="gap"></span><dt>Color</dt><span class="sep"></span><dd>Café</dd></dl>
        </article>
        <article class="product">
          <div class="product-photo product-photo--dark" role="img" aria-label="Foto: sillón Serrano Chair en cuero rojo oscuro"></div>
          <dl class="spec"><dt>Marca</dt><span class="sep"></span><dd>KESTRO</dd><dt>Diseñador</dt><span class="sep"></span><dd>Anselm Varga 1929</dd><dt>Modelo</dt><span class="sep"></span><dd>Serrano Chair</dd><dt>Acabado</dt><span class="sep"></span><dd>Acero Inox. Frente C/ Natural, Reves C/ Artificial. Esponja A/D</dd><span class="gap"></span><dt>Medidas</dt><span class="sep"></span><dd>Ancho: 77 cms.<br>Fondo: 82 cms.<br>Altura: 76 cms</dd><span class="gap"></span><dt>Color</dt><span class="sep"></span><dd>Rojo</dd></dl>
        </article>
      </div>
      <div class="column">
        <article class="product">
          <div class="product-photo product-photo--dark" role="img" aria-label="Foto: otomana Serrano en cuero negro"></div>
          <dl class="spec"><dt>Marca</dt><span class="sep"></span><dd>KESTRO</dd><dt>Diseñador</dt><span class="sep"></span><dd>Anselm Varga 1929</dd><dt>Modelo</dt><span class="sep"></span><dd>Serrano Otomana</dd><dt>Acabado</dt><span class="sep"></span><dd>Acero Inox. Frente C/ Natural, Reves C/ Artificial. Esponja A/D</dd><span class="gap"></span><dt>Medidas</dt><span class="sep"></span><dd>Ancho: 54 cms.<br>Fondo: 61 cms.<br>Altura: 42 cms</dd><span class="gap"></span><dt>Color</dt><span class="sep"></span><dd>Negro</dd></dl>
        </article>
        <article class="product">
          <div class="product-photo product-photo--white" role="img" aria-label="Foto: otomana Serrano en cuero blanco"></div>
          <dl class="spec"><dt>Marca</dt><span class="sep"></span><dd>KESTRO</dd><dt>Diseñador</dt><span class="sep"></span><dd>Anselm Varga 1929</dd><dt>Modelo</dt><span class="sep"></span><dd>Serrano Otomana</dd><dt>Acabado</dt><span class="sep"></span><dd>Acero Inox. Frente C/ Natural, Reves C/ Artificial. Esponja A/D</dd><span class="gap"></span><dt>Medidas</dt><span class="sep"></span><dd>Ancho: 54 cms.<br>Fondo: 61 cms.<br>Altura: 42 cms</dd><span class="gap"></span><dt>Color</dt><span class="sep"></span><dd>Blanco</dd></dl>
        </article>
        <article class="product">
          <div class="product-photo product-photo--brown" role="img" aria-label="Foto: otomana Serrano en cuero café"></div>
          <dl class="spec"><dt>Marca</dt><span class="sep"></span><dd>KESTRO</dd><dt>Diseñador</dt><span class="sep"></span><dd>Anselm Varga 1929</dd><dt>Modelo</dt><span class="sep"></span><dd>Serrano Otomana</dd><dt>Acabado</dt><span class="sep"></span><dd>Acero Inox. Frente C/ Natural, Reves C/ Artificial. Esponja A/D</dd><span class="gap"></span><dt>Medidas</dt><span class="sep"></span><dd>Ancho: 54 cms.<br>Fondo: 61 cms.<br>Altura: 42 cms</dd><span class="gap"></span><dt>Color</dt><span class="sep"></span><dd>Café</dd></dl>
        </article>
        <article class="product">
          <div class="product-photo product-photo--brown" role="img" aria-label="Foto: otomana Serrano en cuero rojo oscuro"></div>
          <dl class="spec"><dt>Marca</dt><span class="sep"></span><dd>KESTRO</dd><dt>Diseñador</dt><span class="sep"></span><dd>Anselm Varga 1929</dd><dt>Modelo</dt><span class="sep"></span><dd>Serrano Otomana</dd><dt>Acabado</dt><span class="sep"></span><dd>Acero Inox. Frente C/ Natural, Reves C/ Artificial. Esponja A/D</dd><span class="gap"></span><dt>Medidas</dt><span class="sep"></span><dd>Ancho: 54 cms.<br>Fondo: 61 cms.<br>Altura: 42 cms</dd><span class="gap"></span><dt>Color</dt><span class="sep"></span><dd>Rojo</dd></dl>
        </article>
      </div>
    </div>
  </section>

  <section class="page page--right">
    <header class="section-band"><h2 class="section-title">SILLONERIA</h2></header>
    <div class="catalogue">
      <div class="column">
        <article class="product">
          <div class="product-photo product-photo--dark" role="img" aria-label="Foto: diván Serrano Day Bed en cuero negro"></div>
          <dl class="spec"><dt>Marca</dt><span class="sep"></span><dd>KESTRO</dd><dt>Diseñador</dt><span class="sep"></span><dd>Anselm Varga 1929</dd><dt>Modelo</dt><span class="sep"></span><dd>Serrano Day Bed</dd><dt>Acabado</dt><span class="sep"></span><dd>Acero Inox. Frente C/ Natural, Reves C/ Artificial. Esponja A/D</dd><span class="gap"></span><dt>Medidas</dt><span class="sep"></span><dd>Ancho: 80 cms.<br>Fondo: 190 cms.<br>Altura: 50 cms</dd><span class="gap"></span><dt>Color</dt><span class="sep"></span><dd>Negro</dd></dl>
        </article>
        <article class="product">
          <div class="product-photo product-photo--brown" role="img" aria-label="Foto: sofá Serrano de dos puestos en cuero oscuro"></div>
          <dl class="spec"><dt>Marca</dt><span class="sep"></span><dd>KESTRO</dd><dt>Diseñador</dt><span class="sep"></span><dd>Anselm Varga 1929</dd><dt>Modelo</dt><span class="sep"></span><dd>Serrano Chair 2 Puestos</dd><dt>Acabado</dt><span class="sep"></span><dd>Acero Inox. Frente C/ Natural, Reves C/ Artificial. Esponja A/D</dd><span class="gap"></span><dt>Medidas</dt><span class="sep"></span><dd>Ancho: 152 cms.<br>Fondo: 82 cms.<br>Altura: 76 cms</dd><span class="gap"></span><dt>Color</dt><span class="sep"></span><dd>Negro</dd></dl>
        </article>
        <article class="product">
          <div class="product-photo product-photo--white" role="img" aria-label="Foto: sofá Serrano de dos puestos en cuero blanco"></div>
          <dl class="spec"><dt>Marca</dt><span class="sep"></span><dd>KESTRO</dd><dt>Diseñador</dt><span class="sep"></span><dd>Anselm Varga 1929</dd><dt>Modelo</dt><span class="sep"></span><dd>Serrano Chair 2 Puestos</dd><dt>Acabado</dt><span class="sep"></span><dd>Acero Inox. Frente C/ Natural, Reves C/ Artificial. Esponja A/D</dd><span class="gap"></span><dt>Medidas</dt><span class="sep"></span><dd>Ancho: 152 cms.<br>Fondo: 82 cms.<br>Altura: 76 cms</dd><span class="gap"></span><dt>Color</dt><span class="sep"></span><dd>Blanco</dd></dl>
        </article>
        <article class="product">
          <div class="product-photo product-photo--brown" role="img" aria-label="Foto: sofá Serrano de dos puestos en cuero café"></div>
          <dl class="spec"><dt>Marca</dt><span class="sep"></span><dd>KESTRO</dd><dt>Diseñador</dt><span class="sep"></span><dd>Anselm Varga 1929</dd><dt>Modelo</dt><span class="sep"></span><dd>Serrano Chair 2 Puestos</dd><dt>Acabado</dt><span class="sep"></span><dd>Acero Inox. Frente C/ Natural, Reves C/ Artificial. Esponja A/D</dd><span class="gap"></span><dt>Medidas</dt><span class="sep"></span><dd>Ancho: 152 cms.<br>Fondo: 82 cms.<br>Altura: 76 cms</dd><span class="gap"></span><dt>Color</dt><span class="sep"></span><dd>Café</dd></dl>
        </article>
      </div>
      <div class="column">
        <article class="product">
          <div class="product-photo product-photo--dark" role="img" aria-label="Foto: butaca cúbica LM3 de un puesto en cuero negro"></div>
          <dl class="spec"><dt>Marca</dt><span class="sep"></span><dd>KESTRO</dd><dt>Diseñador</dt><span class="sep"></span><dd>Lucien Moreau 1929</dd><dt>Modelo</dt><span class="sep"></span><dd>LM3 Armchair 1 Puesto</dd><dt>Acabado</dt><span class="sep"></span><dd>Acero Inox. Frente C/ Natural, Reves C/ Artificial. Esponja A/D</dd><span class="gap"></span><dt>Medidas</dt><span class="sep"></span><dd>Ancho: 99 cms.<br>Fondo: 68 cms.<br>Altura: 73 cms</dd><span class="gap"></span><dt>Color</dt><span class="sep"></span><dd>Negro</dd></dl>
        </article>
        <article class="product">
          <div class="product-photo product-photo--dark" role="img" aria-label="Foto: sofá cúbico LM3 de dos puestos en cuero negro"></div>
          <dl class="spec"><dt>Marca</dt><span class="sep"></span><dd>KESTRO</dd><dt>Diseñador</dt><span class="sep"></span><dd>Lucien Moreau 1929</dd><dt>Modelo</dt><span class="sep"></span><dd>LM3 Loveseat 2 Puestos</dd><dt>Acabado</dt><span class="sep"></span><dd>Acero Inox. Frente C/ Natural, Reves C/ Artificial. Esponja A/D</dd><span class="gap"></span><dt>Medidas</dt><span class="sep"></span><dd>Ancho: 159 cms.<br>Fondo: 68 cms.<br>Altura: 73 cms</dd><span class="gap"></span><dt>Color</dt><span class="sep"></span><dd>Negro</dd></dl>
        </article>
        <article class="product">
          <div class="product-photo product-photo--dark" role="img" aria-label="Foto: sofá cúbico LM3 de tres puestos en cuero negro"></div>
          <dl class="spec"><dt>Marca</dt><span class="sep"></span><dd>KESTRO</dd><dt>Diseñador</dt><span class="sep"></span><dd>Lucien Moreau 1929</dd><dt>Modelo</dt><span class="sep"></span><dd>LM3 Armchair 3 Puestos</dd><dt>Acabado</dt><span class="sep"></span><dd>Acero Inox. Frente C/ Natural, Reves C/ Artificial. Esponja A/D</dd><span class="gap"></span><dt>Medidas</dt><span class="sep"></span><dd>Ancho: 219 cms.<br>Fondo: 68 cms.<br>Altura: 73 cms</dd><span class="gap"></span><dt>Color</dt><span class="sep"></span><dd>Negro</dd></dl>
        </article>
        <article class="product">
          <div class="product-photo product-photo--brown" role="img" aria-label="Foto: butaca cúbica LM2 de un puesto en cuero café"></div>
          <dl class="spec"><dt>Marca</dt><span class="sep"></span><dd>KESTRO</dd><dt>Diseñador</dt><span class="sep"></span><dd>Lucien Moreau 1929</dd><dt>Modelo</dt><span class="sep"></span><dd>LM2 Loveseat 1 Puesto</dd><dt>Acabado</dt><span class="sep"></span><dd>Acero Inox. Frente C/ Natural, Reves C/ Artificial. Esponja A/D</dd><span class="gap"></span><dt>Medidas</dt><span class="sep"></span><dd>Ancho: 54 cms.<br>Fondo: 61 cms.<br>Altura: 42 cms</dd><span class="gap"></span><dt>Color</dt><span class="sep"></span><dd>Café</dd></dl>
        </article>
      </div>
    </div>
  </section>

</main>
</body>
</html>
```